Book Cover - Biography of Dorian and Celeste Whitlock

I am writing a biography about Dorian and Celeste Whitlock. I need a book cover designed for this. The title of the book is: The Remarkable Journeys of Dorian and Celeste Whitlock. I need one version for Ebook with size of 2000px wide by 3200px high and one version for audiobook with size of 3200px wide by 3200px high. *NOTE: Please only use non-copywrite images (open source / royalty-free.)

```html
<!DOCTYPE html>
<html lang="en">
<head>
<meta charset="utf-8">
<title>The Remarkable Journeys of Dorian and Celeste Whitlock — Book Cover</title>
<link rel="stylesheet" href="https://fonts.googleapis.com/css2?family=Questrial&display=swap">
<style>
  :root {
    --backdrop: #3e4346;
    --paper: #ffffff;
    --ink: #1a1617;
    --frame: #3e4547;
    --accent-rose: #bc8286;
    --portrait-dark: #1c1c1e;
    --portrait-mid: #6e6e72;
    --portrait-red: #c8263f;
  }
  * { margin: 0; padding: 0; box-sizing: border-box; }
  html, body {
    width: 1200px;
    height: 1200px;
    overflow: hidden;
    background: var(--backdrop);
  }
  .stage {
    position: relative;
    width: 1200px;
    height: 1200px;
    display: flex;
    align-items: center;
    justify-content: center;
  }
  .book-cover {
    width: 638px;
    height: 960px;
    background: var(--paper);
    display: block;
  }
  .cover-text {
    font-family: "Questrial", "Century Gothic", sans-serif;
    fill: var(--ink);
  }
  .series-line { font-size: 47px; }
  .name-primary { font-size: 90px; }
  .name-secondary { font-size: 90px; }
  .conjunction { font-size: 32px; }
  .surname { font-size: 31px; }
</style>
</head>
<body>
<main class="stage">
  <svg class="book-cover" viewBox="0 0 638 960" xmlns="http://www.w3.org/2000/svg">
    <defs>
      <linearGradient id="portrait-tone" x1="0" y1="0" x2="1" y2="1">
        <stop offset="0" stop-color="var(--portrait-mid)"/>
        <stop offset="0.45" stop-color="var(--portrait-dark)"/>
        <stop offset="0.8" stop-color="var(--portrait-red)"/>
        <stop offset="1" stop-color="var(--portrait-red)"/>
      </linearGradient>
    </defs>

    <!-- lower rose wave band -->
    <path class="wave-band" fill="var(--accent-rose)"
      d="M0,875 C80,830 200,815 320,812 C430,810 520,780 580,720 C610,690 630,660 638,642 L638,960 L0,960 Z"/>

    <!-- series line -->
    <text class="cover-text series-line" x="319" y="86" text-anchor="middle">The Remarkable Journeys of</text>

    <!-- heart frame with portrait area -->
    <g class="heart-frame" transform="translate(85,129)">
      <path fill="var(--frame)"
        d="M234,55 C190,10 100,0 50,40 C0,85 10,190 80,260 C140,320 200,350 234,363 C268,350 328,320 388,260 C458,190 468,85 418,40 C368,0 278,10 234,55 Z"/>
      <g transform="translate(234,190) scale(0.885) translate(-234,-190)">
        <path fill="var(--paper)"
          d="M234,55 C190,10 100,0 50,40 C0,85 10,190 80,260 C140,320 200,350 234,363 C268,350 328,320 388,260 C458,190 468,85 418,40 C368,0 278,10 234,55 Z"/>
      </g>
      <g transform="translate(234,190) scale(0.86) translate(-234,-190)">
        <path role="img" aria-label="Portrait photograph of Dorian and Celeste Whitlock smiling together" fill="url(#portrait-tone)"
          d="M234,55 C190,10 100,0 50,40 C0,85 10,190 80,260 C140,320 200,350 234,363 C268,350 328,320 388,260 C458,190 468,85 418,40 C368,0 278,10 234,55 Z"/>
      </g>
    </g>

    <!-- names -->
    <text class="cover-text name-primary" x="93" y="580">Dorian</text>
    <text class="cover-text conjunction" x="362" y="580">and</text>
    <text class="cover-text name-secondary" x="171" y="665">Celeste</text>
    <text class="cover-text surname" x="540" y="712" text-anchor="end">Whitlock</text>
  </svg>
</main>
</body>
</html>
```